Wine Radio Show web re-design

We need new website look for an unconventional, nationally-syndicated WINE RADIO show. Show is fun, hip, witty and covers all wine lifestyle topics. We are redesigning logo and looking for a redesign of our wordpress site that hosts all our audio podcasts, and the site design needs to leverage and maximize these podcasts. Do NOT use the logo currently on the website. The site is vinecorridor.com, please see more info on the attached.

Do NOT use the logo currently on the website. Please just typeset the name "Cellar Murmurs Radio".
Updates

Please do NOT use the logo from the current website. Please just use type (to match theme/deisgn) "Cellar Murmurs Radio". Thank you.

Hello Designers, Thank you for working on this project. A piece of feedback overall is that we'd like much less image/masthead space in general (the photos and images at the top). We'd like the navigation and the latest Cellar Murmurs podcast to be above the fold. Most of the wine imagery/scenery shots can be minimalized/drastically reduced/eliminated, to allow more room for the different sections. Hope that makes sense, and again, thank you for working on this!! Ruth

Target Market(s)

Wine lovers and wine industry professionals, probably 30+ years old

Industry/Entity Type

Radio

Font styles to use
Serif
Sans Serif
Decorative
Other font styles liked:
• Modern retro fonts

Requirements
Must have
• Must keep current content of site:
http://cellarmurmursradio.com/podcast/
Feature podcasts prominently.
Do NOT use the logo currently on the website.
Nice to have
• Graphics to consider incorporating:
• WINE: Grapes, wine glasses, wine bottles, wine pouring, corkscrews, grapevines, vineyards
• RADIO symbols: soundwaves, antenna, radio icon, Podcast symbols, microphone
Should not have
• Do NOT use current logo - just use type.

```html
<!DOCTYPE html>
<html lang="en">
<head>
<meta charset="utf-8">
<title>Cellar Murmurs Radio</title>
<link rel="stylesheet" href="https://fonts.googleapis.com/css2?family=IM+Fell+English:ital@0;1&family=Raleway:wght@400;500;600;800&display=swap">
<style>
:root{
  --sidebar:#560405;
  --wine:#6b1428;
  --gold:#d49a2a;
  --text:#2a2a2a;
  --muted:#8a8a8a;
  --cream:#f5f1ea;
  --cream-line:#d9cfbf;
  --band:rgba(20,14,10,.85);
  --rule:rgba(255,255,255,.22);
}
*{box-sizing:border-box;margin:0;padding:0}
html,body{width:894px;height:1200px;overflow:hidden;background:#fff}
body{position:relative;font-family:'Raleway',sans-serif;color:var(--text)}
.abs{position:absolute}

.hero{left:0;top:0;width:894px;height:190px;
  background:linear-gradient(180deg,#d8bc66 0%,#c9a54a 40%,#8a6e2c 75%,#4a3a18 100%)}
.hero-band{left:273px;top:136px;width:621px;height:54px;background:var(--band)}
.hero-title{left:290px;top:145px;font-family:'IM Fell English',serif;font-style:italic;font-size:28px;color:#fff;letter-spacing:1px;white-space:nowrap}
.hero-arrows{left:776px;top:152px}

.sidebar-cap{left:75px;top:64px}
.sidebar{left:75px;top:116px;width:198px;height:1084px;background:var(--sidebar)}
.brand-mark{left:163px;top:99px;width:22px;height:22px;border-radius:50%;background:#fff}
.brand{left:75px;top:160px;width:198px;text-align:center;color:#fff}
.brand-name{font-weight:800;font-size:13.5px;letter-spacing:.2px;white-space:nowrap}
.brand-tag{font-size:10px;margin-top:4px}

.menu{left:94px;width:160px;list-style:none;text-align:center;color:#fff}
.menu li{border-bottom:1px solid var(--rule);height:30px;line-height:30px;white-space:nowrap}
.nav{top:211px;font-family:'IM Fell English',serif;font-size:12.5px}
.archives-title{left:75px;top:494px;width:198px;text-align:center;color:#fff;font-family:'IM Fell English',serif;font-size:19px}
.archives{top:527px;font-size:10.5px;letter-spacing:.3px}

.fan-box{left:93px;top:888px;width:161px;height:133px;background:#fff;padding:3px}
.fan-box div{width:100%;height:100%;background:linear-gradient(180deg,#eef1f6,#d8cbbd)}
.newsletter{left:93px;top:1038px;color:#fff;width:170px}
.newsletter h3{font-weight:600;font-size:14.5px;letter-spacing:.5px}
.newsletter p{font-size:8.6px;line-height:12px;margin-top:3px;font-weight:500}
.email{left:94px;top:1091px;width:157px;height:20px;background:#fff;font-size:8.5px;line-height:20px;padding-left:8px;color:#444}
.social{left:92px;top:1123px;display:flex;gap:7px}
.social span{width:22px;height:22px;border-radius:50%;background:#fff;display:block}

.intro-title{left:290px;top:210px;font-weight:500;font-size:23px;letter-spacing:.5px;color:#111;white-space:nowrap}
.intro-title em{font-style:normal;color:var(--wine)}
.intro-image{left:290px;top:250px;width:200px;height:127px;
  background:linear-gradient(160deg,#c8922e,#e8c370 40%,#6a4a1e 75%,#3b4a1a)}
.intro-text{left:503px;top:247px;width:318px;font-size:9.7px;line-height:15px;color:#333}
.btn{background:var(--wine);color:#fff;font-size:12.5px;letter-spacing:.5px;text-align:center;border-radius:2px}
.btn-intro{left:503px;top:349px;width:148px;height:28px;line-height:28px}

h2{font-weight:500;font-size:16px;color:#111;letter-spacing:.3px;white-space:nowrap}
.perspiciatis-title{left:290px;top:412px}
.perspiciatis-text{left:290px;top:435px;width:530px;font-size:9.7px;line-height:15px;color:#333}
.perspiciatis-text span{color:var(--wine)}
.player{left:290px;top:478px;width:530px;height:21px}

.list-title{left:290px;top:546px}
.points{left:290px;top:575px;list-style:none;font-size:11.2px;color:var(--wine)}
.points li{height:22.4px;padding-left:15px;position:relative;white-space:nowrap}
.points li::before{content:"";position:absolute;left:1px;top:5px;width:5px;height:5px;background:var(--gold);transform:rotate(45deg)}
.btn-list{left:291px;top:701px;width:124px;height:27px;line-height:27px}

.episodes{left:589px;top:550px;width:229px;height:184px;background:var(--cream);border:1px solid var(--cream-line);outline:1px solid var(--cream-line);outline-offset:-4px}
.episodes-art{left:756px;top:542px;width:52px;height:48px;background:linear-gradient(180deg,#d9d2c6,#a59a88);border-radius:4px}
.episodes-title{left:606px;top:556px;font-family:'IM Fell English',serif;font-size:18px;color:#4a3c2c}
.episodes-rule{left:606px;top:580px;width:142px;height:1px;background:var(--cream-line)}
.episodes-head{left:606px;top:595px;width:206px;font-size:10.2px;line-height:15px;color:#111;font-weight:500}
.episodes-body{left:606px;top:634px;width:206px;font-size:9.6px;line-height:15px;color:var(--muted)}
.watch{left:608px;top:703px;font-size:10.5px;color:var(--wine);display:flex;align-items:center;gap:10px}

.divider{left:290px;top:770px;width:530px;height:1px;background:var(--cream-line)}
.uncorked-title{left:290px;top:784px}
.card{left:292px;top:812px;width:527px;height:78px;background:var(--cream)}
.card-photo{left:302px;top:820px;width:63px;height:51px;background:linear-gradient(160deg,#9bb88a,#c59b7a);border:2px solid #fff}
.card-name{left:376px;top:816px;font-family:'IM Fell English',serif;font-size:15px;color:var(--wine)}
.card-date{left:720px;top:819px;width:85px;text-align:right;font-size:10px;color:var(--wine)}
.card-text{left:376px;top:845px;width:430px;font-size:9.2px;line-height:14px;color:#333}
.card-more{left:720px;top:868px;width:85px;text-align:right;font-size:9.6px;color:var(--wine)}

.footer-rule{left:290px;top:1160px;width:530px;height:1px;background:var(--cream-line)}
.footer-left{left:290px;top:1173px;font-size:8.8px;color:#666}
.footer-nav{left:620px;top:1173px;width:200px;text-align:right;font-size:8.8px;color:#666}
</style>
</head>
<body>

<div class="abs hero" role="img" aria-label="Wine bottle and red wine glass against a golden sunset over vineyards"></div>
<div class="abs hero-band"></div>
<div class="abs hero-title">Cellar Murmurs Radio</div>
<svg class="abs hero-arrows" width="46" height="22" viewBox="0 0 46 22" aria-hidden="true">
  <circle cx="11" cy="11" r="8.5" fill="none" stroke="#fff" stroke-width="1.6"/>
  <path d="M13 7 L9 11 L13 15" fill="none" stroke="#fff" stroke-width="1.6"/>
  <circle cx="33" cy="11" r="8.5" fill="none" stroke="#fff" stroke-width="1.6"/>
  <path d="M31 7 L35 11 L31 15" fill="none" stroke="#fff" stroke-width="1.6"/>
</svg>

<aside>
  <svg class="abs sidebar-cap" width="198" height="56" viewBox="0 0 198 56" aria-hidden="true">
    <path d="M0 56 L0 52 L18 52 C22 30 40 22 62 18 C80 15 90 8 99 3 C108 8 118 15 136 18 C158 22 176 30 180 52 L198 52 L198 56 Z" fill="#560405"/>
  </svg>
  <div class="abs sidebar"></div>
  <div class="abs brand-mark"></div>
  <div class="abs brand">
    <div class="brand-name">Cellar Murmurs Radio</div>
    <div class="brand-tag">Drink And play with us</div>
  </div>

  <ul class="abs menu nav">
    <li>Home</li><li>Episode Achives</li><li>Uncorked</li><li>About the Show</li><li>About the Host</li><li>On the Air</li><li>Blog</li><li>Store</li><li>Contact Us</li>
  </ul>

  <div class="abs archives-title">Archives</div>
  <ul class="abs menu archives">
    <li>June 2014</li><li>May 2014</li><li>April 2014</li><li>March 2014</li><li>February 2014</li><li>January 2014</li><li>December 2013</li><li>November 2013</li><li>October 2013</li><li>September 2013</li><li>August 2013</li>
  </ul>

  <div class="abs fan-box"><div role="img" aria-label="Social fan box with follower thumbnails"></div></div>

  <div class="abs newsletter">
    <h3>Newsletter</h3>
    <p>Lorem ipsum dolor sit amet elit,<br>sed do eiusmod tempor</p>
  </div>
  <div class="abs email">Email address</div>
  <div class="abs social" aria-label="Social links"><span></span><span></span><span></span><span></span><span></span></div>
</aside>

<main>
  <h1 class="abs intro-title">The <em>Cellar Murmurs Radio</em></h1>
  <div class="abs intro-image" role="img" aria-label="Wine barrel, bottles and a glass of white wine at sunset over vineyards"></div>
  <p class="abs intro-text">Sed ut perspiciatis unde omnis iste natus error siT totam rem aperiam, eaque ipsa quae ab illo inventore veritatis et quasi architec to beatae vitae dicta sunt explicabo Nemo enim ipsam voluptat em quia voluptas sit aspernatur aut odit aut fugit sed quuntur ma gni dolores eos qui ratione voluptatem sequi nesciunt Neque por ro quisquam est, qui dolorem ipsum quia dolor sit amet.</p>
  <div class="abs btn btn-intro">Download Now</div>

  <h2 class="abs perspiciatis-title">Sed ut perspiciatis</h2>
  <p class="abs perspiciatis-text">perspiciatis unde omnis iste <span>natus error sit voluptatem</span> accusantium doloremque laudaum, totam rem aperia eaque ipsa quae ab illo inventore veritatis et quasi architecto beatae <span>vitae dicta sunt explicabo.</span></p>
  <svg class="abs player" width="530" height="21" viewBox="0 0 530 21" aria-label="Audio player">
    <rect width="530" height="21" fill="#6b1428"/>
    <circle cx="17" cy="10.5" r="6.5" fill="#fff"/>
    <circle cx="17" cy="10.5" r="5" fill="#111"/>
    <path d="M15.5 8 L19.5 10.5 L15.5 13 Z" fill="#fff"/>
    <rect x="34" y="6" width="252" height="9" fill="#bfb4a7"/>
    <rect x="286" y="6" width="126" height="9" fill="#3a2a2a"/>
    <rect x="412" y="6" width="104" height="9" fill="#fff"/>
  </svg>

  <h2 class="abs list-title">Lorem ipsum dolor sit amet</h2>
  <ul class="abs points">
    <li>Sed ut perspiciatis unde omnis iste natus error sit</li>
    <li>voluptatem accusantium doloremque laudantium</li>
    <li>aperiam, eaque ipsa quae ab illo inventore</li>
    <li>veritatis et quasi architecto beatae vitae dicta sunt</li>
    <li>Nemo enim ipsam voluptatem quia voluptas</li>
  </ul>
  <div class="abs btn btn-list">Download Now</div>

  <section>
    <div class="abs episodes"></div>
    <div class="abs episodes-art" role="img" aria-label="Engraved wine press illustration"></div>
    <div class="abs episodes-title">Episodes</div>
    <div class="abs episodes-rule"></div>
    <p class="abs episodes-head">The Inside Scoop on China's Extraoinary Growth and Passion for Wine</p>
    <p class="abs episodes-body">This week on Cellar Murmurs Radio host Owen Hartley speaks with two of the big-gest experts on the growing popularity of wine in Asia.</p>
    <div class="abs watch">Watch Now
      <svg width="18" height="18" viewBox="0 0 18 18" aria-hidden="true"><circle cx="9" cy="9" r="9" fill="#111"/><path d="M7 5 L13 9 L7 13 Z" fill="#fff"/></svg>
    </div>
  </section>

  <div class="abs divider"></div>
  <h2 class="abs uncorked-title">Uncorked</h2>
  <div class="abs card"></div>
  <div class="abs card-photo" role="img" aria-label="Portrait photo of the guest"></div>
  <div class="abs card-name">Marisol</div>
  <div class="abs card-date">2014.06.09</div>
  <p class="abs card-text">This week on Cellar Murmurs Radio, host Owen Hartley speaks with two of the biggest experts on the growing popularity of wine in Asia.</p>
  <div class="abs card-more">View More</div>
</main>

<footer>
  <div class="abs footer-rule"></div>
  <div class="abs footer-left">(c) 2013 Cellar Murmurs Radio - All right reserve</div>
  <div class="abs footer-nav">Home About Contact Us</div>
</footer>

</body>
</html>
```